Load Up Your Cart

Require two banners with a size of 980 x 450 pixels
Similar natural looking banner as per attachment. The background is supposed to be a cardboard carton
price "$9.95"
Wording and layout the same as attached file

```html
<!DOCTYPE html>
<html lang="en">
<head>
<meta charset="utf-8">
<title>Load Up Your Cart – $9.95 Flat Rate Shipping</title>
<link rel="stylesheet" href="https://fonts.googleapis.com/css2?family=Alfa+Slab+One&family=Anton&family=Special+Elite&display=swap">
<style>
  :root {
    --carton-light: #d9b48e;
    --carton-mid: #cfa67d;
    --carton-dark: #c2956a;
    --stamp-red: #ad1c1e;
    --price-red: #a81a1c;
    --price-shadow: #5e0c0d;
    --ink-brown: #4b3625;
  }
  html, body {
    margin: 0;
    padding: 0;
    width: 1200px;
    height: 551px;
    overflow: hidden;
  }
  .banner {
    position: relative;
    width: 1200px;
    height: 551px;
    background: radial-gradient(ellipse at 55% 40%, var(--carton-light) 0%, var(--carton-mid) 60%, var(--carton-dark) 100%);
  }
  .banner-art {
    position: absolute;
    inset: 0;
    width: 1200px;
    height: 551px;
  }
  .stamp { color: var(--stamp-red); }
  .stamp-ring, .stamp-rule { stroke: currentColor; fill: none; }
  .stamp-headline {
    font-family: "Alfa Slab One", serif;
    fill: currentColor;
  }
  .stamp-subline {
    font-family: "Alfa Slab One", serif;
    fill: currentColor;
    letter-spacing: 3px;
  }
  .price, .price-shadow { font-family: "Anton", sans-serif; }
  .price { fill: var(--price-red); }
  .price-shadow { fill: var(--price-shadow); }
  .offer-title {
    font-family: "Special Elite", monospace;
    fill: var(--price-red);
  }
  .offer-terms {
    font-family: "Special Elite", monospace;
    fill: var(--ink-brown);
  }
</style>
</head>
<body>
<main class="banner">
  <svg class="banner-art" viewBox="0 0 980 450" width="1200" height="551" xmlns="http://www.w3.org/2000/svg">
    <defs>
      <filter id="carton-grain" x="0" y="0" width="100%" height="100%">
        <feTurbulence type="fractalNoise" baseFrequency="0.85" numOctaves="3" seed="4" result="noise"/>
        <feColorMatrix in="noise" type="matrix"
          values="0 0 0 0 0.42
                  0 0 0 0 0.28
                  0 0 0 0 0.16
                  0 0 0 0.55 -0.12"/>
      </filter>
      <filter id="carton-fibres" x="0" y="0" width="100%" height="100%">
        <feTurbulence type="fractalNoise" baseFrequency="0.012 0.08" numOctaves="2" seed="9" result="fibre"/>
        <feColorMatrix in="fibre" type="matrix"
          values="0 0 0 0 0.55
                  0 0 0 0 0.38
                  0 0 0 0 0.22
                  0 0 0 0.35 -0.08"/>
      </filter>
      <filter id="ink-wear">
        <feTurbulence type="fractalNoise" baseFrequency="0.9" numOctaves="2" seed="3" result="wear"/>
        <feColorMatrix in="wear" type="matrix"
          values="0 0 0 0 0
                  0 0 0 0 0
                  0 0 0 0 0
                  0 0 0 -2.2 1.9" result="mask"/>
        <feComposite in="SourceGraphic" in2="mask" operator="in"/>
      </filter>
      <path id="stamp-arc" d="M 50 205 A 150 150 0 0 0 350 205"/>
    </defs>

    <rect class="carton-fibres" width="980" height="450" filter="url(#carton-fibres)"/>
    <rect class="carton-grain" width="980" height="450" filter="url(#carton-grain)"/>

    <g class="stamp" transform="rotate(-17 200 205)" filter="url(#ink-wear)">
      <circle class="stamp-ring" cx="200" cy="205" r="165" stroke-width="8"/>
      <line class="stamp-rule" x1="5" y1="106" x2="425" y2="106" stroke-width="9"/>
      <line class="stamp-rule" x1="5" y1="120" x2="425" y2="120" stroke-width="4"/>
      <line class="stamp-rule" x1="-5" y1="252" x2="435" y2="252" stroke-width="4"/>
      <line class="stamp-rule" x1="-5" y1="266" x2="435" y2="266" stroke-width="9"/>
      <text class="stamp-headline" x="200" y="236" font-size="108" text-anchor="middle" textLength="372" lengthAdjust="spacingAndGlyphs">LOAD UP</text>
      <text class="stamp-subline" font-size="32">
        <textPath href="#stamp-arc" startOffset="50%" text-anchor="middle">YOUR CART</textPath>
      </text>
    </g>

    <g class="price-group" filter="url(#ink-wear)">
      <text class="price-shadow" x="524" y="204" font-size="150" textLength="352" lengthAdjust="spacingAndGlyphs">$ 9.95</text>
      <text class="price" x="520" y="200" font-size="150" textLength="352" lengthAdjust="spacingAndGlyphs">$ 9.95</text>
    </g>

    <text class="offer-title" x="420" y="312" font-size="50" textLength="528" lengthAdjust="spacingAndGlyphs">FLAT RATE SHIPPING</text>
    <text class="offer-terms" x="422" y="364" font-size="28" textLength="524" lengthAdjust="spacingAndGlyphs">NO MINIMUMS. NO CODES. NO GIMMICKS.</text>
  </svg>
</main>
</body>
</html>
```